mapleridgegroup Business Card Design

Business card with logo design for mapleridgegroup. We are a group of professional project managers based on the Pareto Principle that 80% of the work is done by 20% of the people. I have a makeshift logo that uses a pi chart with 30% and 20% and the 20% pie slice is set slightly out and up. Have played around with a teal and orange colour scheme.

Industry/Entity Type

Business

Contact Information for Business Card

Gareth Pembroke
Director
mapleridgegroup

0452 803716

```html
<!DOCTYPE html>
<html lang="en">
<head>
<meta charset="utf-8">
<title>mapleridgegroup Business Card</title>
<link rel="stylesheet" href="https://fonts.googleapis.com/css2?family=Open+Sans:wght@300;400;600;700&display=swap">
<style>
  :root {
    --bg: #4a4a4c;
    --card: #ffffff;
    --orange: #f0683a;
    --orange-light: #f58a4e;
    --teal: #2a9ea5;
    --ink: #ffffff;
    --rule: rgba(255,255,255,0.55);
  }
  * { box-sizing: border-box; margin: 0; padding: 0; }
  html, body { width: 1200px; height: 990px; overflow: hidden; }
  body {
    background: var(--bg);
    font-family: "Open Sans", Arial, sans-serif;
    display: flex;
    align-items: center;
    justify-content: center;
    gap: 80px;
  }
  .card {
    width: 420px;
    height: 700px;
    background: var(--card);
    position: relative;
    box-shadow: 0 14px 30px rgba(0,0,0,0.35);
  }
  /* front */
  .card-front { display: flex; flex-direction: column; }
  .brand-area {
    height: 300px;
    display: flex;
    align-items: center;
    justify-content: center;
    gap: 12px;
  }
  .brand-dot {
    width: 22px; height: 22px;
    border-radius: 50%;
    background: var(--teal);
  }
  .brand-name {
    font-weight: 600;
    font-size: 30px;
    color: var(--teal);
    letter-spacing: 0.5px;
  }
  .contact-panel {
    flex: 1;
    margin: 0 22px 22px 0;
    background: linear-gradient(160deg, var(--orange-light), var(--orange));
    color: var(--ink);
    display: flex;
    flex-direction: column;
    align-items: center;
    padding: 34px 40px 20px;
    text-align: center;
  }
  .person-name {
    font-weight: 700;
    font-size: 26px;
    letter-spacing: 1px;
    text-transform: uppercase;
  }
  .person-role {
    font-weight: 400;
    font-size: 13px;
    letter-spacing: 1.5px;
    text-transform: uppercase;
    margin-top: 2px;
    margin-bottom: 22px;
  }
  .contact-list { list-style: none; width: 100%; }
  .contact-item {
    display: flex;
    flex-direction: column;
    align-items: center;
    gap: 4px;
    padding: 8px 0;
    border-bottom: 1px solid var(--rule);
    font-size: 13px;
  }
  .contact-item:last-child { border-bottom: none; }
  .contact-icon { width: 16px; height: 16px; }
  /* back */
  .card-back {
    border: 30px solid var(--teal);
    display: flex;
    align-items: center;
    justify-content: center;
    gap: 14px;
  }
  .card-back .brand-dot { width: 30px; height: 30px; background: var(--orange); }
  .card-back .brand-name { font-size: 34px; }
</style>
</head>
<body>
  <section class="card card-front">
    <div class="brand-area">
      <span class="brand-dot"></span>
      <span class="brand-name">mapleridgegroup</span>
    </div>
    <div class="contact-panel">
      <h1 class="person-name">Gareth Pembroke</h1>
      <p class="person-role">General Manager</p>
      <ul class="contact-list">
        <li class="contact-item">
          <svg class="contact-icon" viewBox="0 0 16 16"><path d="M4 1.5l2.3 2.6-1.4 1.7c.9 1.9 2.3 3.3 4.2 4.2l1.7-1.4 2.7 2.3-1.2 2.1C7.6 13 3 8.4 2 3.7z" fill="#fff"/></svg>
          <span>0452 803716</span>
        </li>
        <li class="contact-item">
          <svg class="contact-icon" viewBox="0 0 16 16"><rect x="1.5" y="3.5" width="13" height="9" fill="#fff"/><path d="M1.5 3.5L8 9l6.5-5.5" fill="none" stroke="#f0683a" stroke-width="1.2"/></svg>
          <span>hello@mapleridgegroup.com</span>
        </li>
        <li class="contact-item">
          <svg class="contact-icon" viewBox="0 0 16 16"><circle cx="8" cy="8" r="6.5" fill="none" stroke="#fff" stroke-width="1.4"/><path d="M1.5 8h13M8 1.5c-2.5 3-2.5 10 0 13M8 1.5c2.5 3 2.5 10 0 13" fill="none" stroke="#fff" stroke-width="1.1"/></svg>
          <span>www.mapleridgegroup.com</span>
        </li>
        <li class="contact-item">
          <svg class="contact-icon" viewBox="0 0 16 16"><path d="M8 15s5-5.3 5-9A5 5 0 0 0 3 6c0 3.7 5 9 5 9z" fill="#fff"/><circle cx="8" cy="6" r="1.8" fill="#f0683a"/></svg>
          <span>27 Wattle Creek Drive<br>Suite 4</span>
        </li>
      </ul>
    </div>
  </section>

  <section class="card card-back">
    <span class="brand-dot"></span>
    <span class="brand-name">mapleridgegroup</span>
  </section>
</body>
</html>
```